Book Cover design - Education & Research

We need a design of the book cover for a book written in an education sector. It has been written by a professor with target audience being other professors, lecturers, PhD students etc. The book is about Singapore's development as a country (from third world to economical leader) with high emphasis on it's education sector. It explores many education concepts that could set an example for other countries.
We would like the design to be serious, modern, representing innovation, progress in the educations space. The colours will be mainly red and white representing the country's flag. Probably white background with red additions. The design will consist of three parts:
1) Front cover (the most important where the designer should put most effort in). At the top will be name of the author: Zofia Kradecka, below name of the book: "Odlegle Sciezki Nauczania" with smaller subtitle below: "Zielone Mosty Pomiedzy Szkolami Zielone Mosty Pomiedzy Szkolami"
2) Back cover (very simple with majority of the space put for text, reviews etc.)
3) Second page already inside the book (less important, just a simple black and white design in this part)
We welcome any creative designs from your part, but for reference below is an idea of how we would like it to look like. I would recommend for the designers to do two designs. One according to the below instructions and another with your own idea how to go about it. Please do keep in mind that we can't use proprietary Singapore icons like quorvex or exact design of Singapore flag, so please don't use these.
Our idea:
- The front page to have cityscape with silhouettes of Singapore iconic buildings (Coral Hill Towers, Halvern Wheel, Lumen Craft Gallery, Corvanta, Terraces of Wrenfield, Sky scrappers)
- A red and white ribbon starting at the front and then going through the spine of the book to the back cover.
NOTE:
- We would like to see more designs with your own creativity and other colors, not only red and white
Education sector, Universities, Professors

```html
<!DOCTYPE html>
<html lang="pl">
<head>
<meta charset="UTF-8">
<title>Odlegle Sciezki Nauczania — okładka</title>
<link rel="stylesheet" href="https://fonts.googleapis.com/css2?family=Bebas+Neue&family=Oswald:wght@600;700&display=swap">
<style>
  :root {
    --page-bg: #ededed;
    --sky-top: #f4f4f4;
    --sky-bottom: #d2d3d5;
    --flag-red: #e3121b;
    --deep-red: #6f0407;
    --mid-red: #9a0d12;
    --author-ink: #4a0a0c;
    --paper-white: #ffffff;
  }
  html, body {
    margin: 0;
    padding: 0;
    width: 1200px;
    height: 1200px;
    overflow: hidden;
    background: var(--page-bg);
  }
  .book-cover {
    position: absolute;
    left: 250px;
    top: 50px;
    width: 700px;
    height: 1100px;
    overflow: hidden;
    background: linear-gradient(180deg, var(--sky-top) 0%, var(--sky-bottom) 39%);
    box-shadow: 0 10px 30px rgba(0,0,0,0.18);
  }
  .author-name {
    position: absolute;
    top: 48px;
    left: 0;
    width: 100%;
    margin: 0;
    text-align: center;
    font-family: "Oswald", sans-serif;
    font-weight: 700;
    font-size: 44px;
    letter-spacing: 0.42em;
    padding-left: 0.42em;
    box-sizing: border-box;
    color: var(--author-ink);
    line-height: 1;
  }
  .skyline-art {
    position: absolute;
    left: 0;
    top: 180px;
    width: 700px;
    height: 250px;
  }
  .lower-panel {
    position: absolute;
    left: 0;
    top: 430px;
    width: 700px;
    height: 670px;
    background: linear-gradient(180deg, var(--deep-red) 0%, var(--mid-red) 14%, var(--deep-red) 40%, var(--deep-red) 100%);
  }
  .title-block {
    position: absolute;
    top: 500px;
    left: 0;
    width: 100%;
    margin: 0;
    text-align: center;
    font-family: "Bebas Neue", sans-serif;
    font-weight: 400;
    color: var(--paper-white);
    line-height: 0.86;
  }
  .title-lead { display: block; font-size: 80px; }
  .title-main { display: block; font-size: 190px; }
  .title-last { display: block; font-size: 158px; }
  .subtitle {
    position: absolute;
    top: 952px;
    left: 0;
    width: 100%;
    margin: 0;
    text-align: center;
    font-family: "Oswald", sans-serif;
    font-weight: 600;
    font-size: 27px;
    letter-spacing: 0.14em;
    line-height: 1.75;
    color: var(--paper-white);
  }
</style>
</head>
<body>
  <div class="book-cover">
    <p class="author-name">ZOFIA KRADECKA</p>

    <svg class="skyline-art" viewBox="0 0 700 250" role="img" aria-label="Red city skyline silhouette with Coral Hill Towers, Halvern Wheel, Lumen Craft Gallery and a flowing red and white ribbon under white clouds">
      <defs>
        <linearGradient id="skylineTone" x1="0" y1="0" x2="0" y2="1">
          <stop offset="0" stop-color="#d9dadc" stop-opacity="0"/>
          <stop offset="0.35" stop-color="#f2d6d7"/>
          <stop offset="0.7" stop-color="#e8474d"/>
          <stop offset="1" stop-color="#c8141b"/>
        </linearGradient>
      </defs>
      <rect x="0" y="0" width="700" height="250" fill="url(#skylineTone)"/>
    </svg>

    <div class="lower-panel"></div>

    <h1 class="title-block">
      <span class="title-lead">ODLEGLE</span>
      <span class="title-main">SCIEZKI</span>
      <span class="title-last">NAUCZANIA</span>
    </h1>

    <p class="subtitle">ZIELONE MOSTY POMIEDZY SZKOLAMI<br>ZIELONE MOSTY POMIEDZY SZKOLAMI</p>
  </div>
</body>
</html>
```